Flyer for the Harvest of lanterns conference

Flyer design for an annual international conference called "VELMARK 2017". This is a conference for young adults, so we hope to produce a design that is both professional and appealing to young people in general

We'd like the flyer to showcase the conference brand logo, and clearly highlight the key information to people who will read it.

Target Market(s)

Young people, young adults

Industry/Entity Type

Religious

Font styles to use
Sans Serif

Colors

Designer to choose colors to be used in the design.

Requirements
Must have
• - Should be only one page (Vertical or Horizontal).
• - the VELMAK logo and all the information found in the attached text file. This includes: Main topic: Your sons and daughters shall prophesy,
• Dates and time, location, contact information and everything that is in the attached text file.
Nice to have
• It would be nice to see samples where the white logo is used and another where the black one is used.
Should not have
• This is NOT a folded flyer, we will be sticking it on doors and public places. And we will be printing large simple to put on walls. So only one page with few words like an add (the words are in the attached file)

```html
<!DOCTYPE html>
<html lang="en">
<head>
<meta charset="utf-8">
<title>VELMARK 2017 — Harvest of Lanterns Conference</title>
<link href="https://fonts.googleapis.com/css2?family=Cinzel:wght@500;700&family=Open+Sans:wght@400;600;700&display=swap" rel="stylesheet">
<style>
  :root {
    --canvas: #a9a9a9;
    --maroon: #5a0000;
    --maroon-deep: #4a0000;
    --title-red: #6a0b0b;
    --gold: #f0b54c;
    --amber: #e89b1c;
    --ink: #3e3e3e;
    --white: #ffffff;
    --row-light: #ffffff;
    --row-shade: #eeeeee;
  }
  * { box-sizing: border-box; margin: 0; padding: 0; }
  html, body { width: 1200px; height: 1200px; overflow: hidden; }
  body {
    background: radial-gradient(circle at 50% 45%, #c4c4c4 0%, var(--canvas) 70%);
    font-family: "Open Sans", Arial, sans-serif;
    position: relative;
  }
  .flyer {
    position: absolute;
    left: 253px; top: 110px;
    width: 694px; height: 981px;
    background: var(--white);
    overflow: hidden;
  }
  .hero {
    position: absolute; left: 0; top: 0; width: 694px; height: 415px;
    background:
      radial-gradient(ellipse 38% 55% at 54% 100%, #5a0c04 0%, #7a1a06 45%, rgba(122,26,6,0) 100%),
      radial-gradient(ellipse 60% 40% at 60% 5%, #fff6c8 0%, rgba(255,230,140,0) 100%),
      linear-gradient(180deg, #f7c04a 0%, #f2a52e 35%, #e07f1c 65%, #b3510f 100%);
  }
  .logo-card {
    position: absolute; left: 57px; top: 0; width: 166px; height: 148px;
    background: var(--white);
    border-radius: 0 0 10px 10px;
    display: flex; flex-direction: column; align-items: center; justify-content: center; gap: 12px;
  }
  .logo-card .mark {
    width: 76px; height: 76px; border-radius: 50%;
    border: 2px solid var(--amber);
  }
  .logo-card .name {
    font-family: "Open Sans", Arial, sans-serif;
    font-weight: 700; font-size: 22px; letter-spacing: 2px; color: #1a1a1a;
  }
  .event-title {
    position: absolute; left: 257px; top: 44px;
    font-family: "Cinzel", Georgia, serif; color: var(--title-red);
  }
  .event-title h1 { font-size: 42px; font-weight: 700; line-height: 1.1; }
  .event-title p { font-size: 21px; font-weight: 700; margin-top: 2px; letter-spacing: .3px; }
  .tagline {
    position: absolute; left: 174px; top: 365px; width: 346px; height: 28px;
    border-top: 1px solid rgba(255,255,255,.85);
    border-bottom: 1px solid rgba(255,255,255,.85);
    color: var(--white); font-family: "Cinzel", Georgia, serif; font-size: 13.5px; font-weight: 500;
    display: flex; align-items: center; justify-content: center; white-space: nowrap;
  }
  .speakers {
    position: absolute; left: 0; top: 415px; width: 694px; height: 203px; background: var(--maroon);
  }
  .speakers h2 {
    position: absolute; left: 170px; top: 0; width: 354px; height: 46px;
    background: linear-gradient(90deg, rgba(74,0,0,0) 0%, var(--maroon-deep) 20%, var(--maroon-deep) 80%, rgba(74,0,0,0) 100%);
    font-family: "Cinzel", Georgia, serif; font-weight: 500; font-size: 29px; color: var(--gold);
    display: flex; align-items: center; justify-content: center;
  }
  .speaker {
    position: absolute; display: flex; align-items: center; gap: 8px;
    color: var(--white); font-weight: 700; font-size: 17px; white-space: nowrap;
  }
  .speaker svg { width: 17px; height: 17px; flex: none; }
  .speaker span { padding: 4px 0 6px; }
  .speaker.ruled span { border-bottom: 1px solid rgba(255,255,255,.8); }
  .info-row {
    position: absolute; left: 0; width: 694px;
    background: linear-gradient(180deg, var(--row-light) 0%, var(--row-shade) 100%);
  }
  .info-row .icon { position: absolute; left: 106px; width: 26px; height: 26px; }
  .info-row .label { position: absolute; left: 154px; font-weight: 600; font-size: 17px; color: var(--amber); }
  .info-row .value { position: absolute; left: 275px; font-size: 17px; color: var(--ink); line-height: 21px; }
  .footer { position: absolute; left: 0; top: 894px; width: 694px; height: 87px; background: var(--maroon); }
  .footer .contact-tab { position: absolute; left: 0; top: 0; width: 190px; height: 87px; }
  .footer .contact-label {
    position: absolute; left: 64px; top: 16px; font-weight: 700; font-size: 21px; line-height: 25px; color: var(--title-red);
  }
  .footer .phone {
    position: absolute; left: 200px; right: 0; top: 12px;
    display: flex; justify-content: center; align-items: center; gap: 14px;
    color: var(--white); font-weight: 700; font-size: 24px;
  }
  .footer .phone svg { width: 30px; height: 24px; }
  .footer .links {
    position: absolute; left: 200px; right: 0; top: 56px; text-align: center;
    color: var(--white); font-size: 13.5px;
  }
</style>
</head>
<body>
  <article class="flyer">
    <section class="hero" role="img" aria-label="Photo: person seated on a mountain peak above golden, sunlit mountain ranges"></section>

    <div class="logo-card">
      <div class="mark"></div>
      <div class="name">VELMAK</div>
    </div>

    <header class="event-title">
      <h1>VELMARK 2017</h1>
      <p>Harvest of Lanterns Conference</p>
    </header>

    <div class="tagline">Your sons and daughters shall prophesy</div>

    <section class="speakers">
      <h2>Speakers:</h2>
      <div class="speaker ruled" style="left:74px; top:66px;">
        <svg viewBox="0 0 20 20"><circle cx="10" cy="10" r="8.5" fill="none" stroke="#f0b54c" stroke-width="1.4"/><path d="M6 10.2l2.7 2.6L14 7.6" fill="none" stroke="#f0b54c" stroke-width="1.4"/></svg>
        <span style="width:260px">Prophet Laurent Mbeki</span>
      </div>
      <div class="speaker ruled" style="left:74px; top:102px;">
        <svg viewBox="0 0 20 20"><circle cx="10" cy="10" r="8.5" fill="none" stroke="#f0b54c" stroke-width="1.4"/><path d="M6 10.2l2.7 2.6L14 7.6" fill="none" stroke="#f0b54c" stroke-width="1.4"/></svg>
        <span style="width:260px">Bishop Samuel Dorane</span>
      </div>
      <div class="speaker" style="left:74px; top:138px;">
        <svg viewBox="0 0 20 20"><circle cx="10" cy="10" r="8.5" fill="none" stroke="#f0b54c" stroke-width="1.4"/><path d="M6 10.2l2.7 2.6L14 7.6" fill="none" stroke="#f0b54c" stroke-width="1.4"/></svg>
        <span>Prophet Joel Aaron Tshilenge</span>
      </div>
      <div class="speaker ruled" style="left:390px; top:66px;">
        <svg viewBox="0 0 20 20"><circle cx="10" cy="10" r="8.5" fill="none" stroke="#f0b54c" stroke-width="1.4"/><path d="M6 10.2l2.7 2.6L14 7.6" fill="none" stroke="#f0b54c" stroke-width="1.4"/></svg>
        <span style="width:176px">Prophet Noel Varent</span>
      </div>
      <div class="speaker ruled" style="left:390px; top:102px;">
        <svg viewBox="0 0 20 20"><circle cx="10" cy="10" r="8.5" fill="none" stroke="#f0b54c" stroke-width="1.4"/><path d="M6 10.2l2.7 2.6L14 7.6" fill="none" stroke="#f0b54c" stroke-width="1.4"/></svg>
        <span style="width:176px">Prophet Marc Ilunda</span>
      </div>
    </section>

    <section class="info-row" style="top:618px; height:99px;">
      <svg class="icon" style="top:34px" viewBox="0 0 26 26" fill="none" stroke="#e89b1c" stroke-width="1.3"><rect x="2" y="4" width="22" height="20" rx="1"/><path d="M2 9h22M7 2v4M19 2v4"/><path d="M5 13h16M5 17h16M5 21h16M9 11v12M13 11v12M17 11v12" stroke-width=".8"/></svg>
      <div class="label" style="top:35px">Date:</div>
      <div class="value" style="top:35px">September 1st, 2nd and 3rd 2017<br>Start Time: 6:00PM</div>
    </section>

    <section class="info-row" style="top:717px; height:98px;">
      <svg class="icon" style="top:15px" viewBox="0 0 26 26" fill="none" stroke="#e89b1c" stroke-width="1.3"><path d="M13 20s-6-6.5-6-11a6 6 0 0112 0c0 4.5-6 11-6 11z"/><circle cx="13" cy="9" r="2.2"/><path d="M9 19c-4 .6-7 1.8-7 3 0 1.6 5 2.8 11 2.8s11-1.2 11-2.8c0-1.2-3-2.4-7-3"/></svg>
      <div class="label" style="top:16px">Location:</div>
      <div class="value" style="top:14px">Harborlight Lodge &amp; Suites<br>415 Elmwood Avenue<br>Westbrook, ME 04092 United States</div>
    </section>

    <section class="info-row" style="top:815px; height:79px;">
      <svg class="icon" style="top:15px" viewBox="0 0 26 26" fill="none" stroke="#e89b1c" stroke-width="1.3"><rect x="2" y="8" width="22" height="16"/><rect x="8" y="2" width="10" height="6"/><path d="M5 12h16M5 16h16M5 20h16M9 10v12M13 10v12M17 10v12" stroke-width=".8"/></svg>
      <div class="label" style="top:17px">Room:</div>
      <div class="value" style="top:17px; left:273px">Cedarfield Ballroom</div>
    </section>

    <footer class="footer">
      <svg class="contact-tab" viewBox="0 0 190 87" preserveAspectRatio="none"><polygon points="0,0 190,0 157,87 0,87" fill="#f0b54c"/></svg>
      <div class="contact-label">Contact<br>Info:</div>
      <div class="phone">
        <svg viewBox="0 0 30 24" fill="#f0b54c"><path d="M2 8c0-4 6-6 13-6s13 2 13 6v2h-6V7c-2-.8-4.5-1-7-1s-5 .2-7 1v3H2z"/><path d="M9 10h12l5 12H4z"/><circle cx="15" cy="16" r="3" fill="#5a0000"/></svg>
        <span>+1 (555) 012 3487</span>
      </div>
      <div class="links">Email:hello@lanternhall.org - Website: http://velmak-events.org</div>
    </footer>
  </article>
</body>
</html>
```